Avocado Smoothies (100% Natural, No Preservatives, No added Sugar)

We need a company logo (for business cards etc) as well as label design (front and back) for a range of avocado based smoothies on our 300 ml bottle & pouch with drinking spout. The look & feel of the label is that the smoothies are fresh & healthy, prepared with freshest ingredients & formulated with nutritional needs in mind.

The final design should give the impression of a genuine & trusted brand of beverage that is appealing to (1) health conscious busy professionals both male & female (e.g. gym / yoga / athletic buffs), (2) busy mothers of fussy / picky kids; and (3) people who like more plant-based diets, who want the best products for them / their families. The design is to be innovative & appealing to the intelligent health conscious consumers especially avocado fans, looking for healthier alternatives of natural drinks on-the go, that are NOT prepared by big, impersonal & highly automated factories that use all sorts of nasties & processes in their beverages. Easy to read FONT and preferably include an original picture of avocado (which can be a real picture / graphic design) - however, this is not necessary.

Company name: OWRU Pte.Ltd. (the letter "I" may mean "I" or "Innovative" or "Intelligent". "OWRU" can be a play of the word "I ever .... " e.g. "all OWRU wanted is ... ".)

Please note that the master label design should be versatile enough for a range of avocado smoothies (we only need to make minimum changes to the main picture / words as necessary for each specific avocado smoothie) and the label can also be used for kids size and adult size pouches and bottles of height 16cm and diameter of circular base of 5.5cm.

Target Market(s)

(1) health conscious busy professionals (e.g. gym / yoga / athletic buffs), (2) busy mothers of fussy / picky kids; and (3) vegans & people who like more plant based diets, who want the best products for them / their families.

Logo Text

OWRU

Font styles to use
Serif
Sans Serif
Decorative
Script

Colors

Designer to choose colors to be used in the design.

Requirements
Must have
• Centre attention of the label (BIG font): Avocado & [we insert the other main ingredients] Smoothie
• Company logo (noticeable somewhere on the label): OWRU
• (Medium font) All natural ingredients, no added sugar or salt, no additives or preservatives
• (Smaller fonts) Along the lines of: "Made from the finest blend of avocados and [we can insert other ingredients] to nourish you. Rich, creamy, wholesome & unique avocado experience that is good and satisfyingly delicious! "
• Keep refrigerated below 5 deg C
• Manufactured by: [we insert details]
• 300ml
Nice to have
• Please recycle usual logo
• originality & fresh & appealing factor
Should not have
• unhealthy image / junk food / sugary / additives / unsavoury impression
• difficult to read font
• confusion with other existing brands

```html
<!DOCTYPE html>
<html lang="en">
<head>
<meta charset="UTF-8">
<title>OWRU Avocado Smoothie Label</title>
<link href="https://fonts.googleapis.com/css2?family=Oswald:wght@400;500;700&family=Pacifico&display=swap" rel="stylesheet">
<style>
  :root {
    --bg: #e9e9e9;
    --label: #ffffff;
    --ink: #2a2a2a;
    --green: #5b9a2c;
    --green-dark: #3f7a1e;
    --green-light: #8cc152;
    --band-text: #ffffff;
  }
  * { margin: 0; padding: 0; box-sizing: border-box; }
  html, body {
    width: 1200px; height: 960px; overflow: hidden;
    background: var(--bg);
    font-family: "Oswald", "Arial Narrow", sans-serif;
  }
  .label {
    position: absolute;
    left: 340px; top: 40px;
    width: 520px; height: 880px;
    background: var(--label);
    box-shadow: 0 2px 10px rgba(0,0,0,0.08);
    overflow: hidden;
  }
  .brand {
    position: absolute; top: 70px; left: 0; width: 100%;
    display: flex; justify-content: center; align-items: center; gap: 12px;
  }
  .brand-name {
    font-family: "Oswald", sans-serif; font-weight: 500;
    font-size: 54px; letter-spacing: 4px; color: var(--ink); line-height: 1;
  }
  .brand-dot {
    width: 18px; height: 18px; border-radius: 50%; background: var(--green);
  }
  .product-name {
    position: absolute; top: 150px; width: 100%; text-align: center;
    font-weight: 700; font-size: 116px; line-height: 1; color: var(--ink);
    letter-spacing: -1px;
  }
  .product-type {
    position: absolute; top: 262px; width: 100%; text-align: center;
    font-family: "Pacifico", cursive; font-size: 66px; line-height: 1;
    color: var(--green);
  }
  .flavour {
    position: absolute; top: 350px; width: 100%; text-align: center;
    font-weight: 500; font-size: 34px; line-height: 1; color: var(--ink);
  }
  .hero {
    position: absolute; left: 120px; top: 410px;
    width: 290px; height: 290px; border-radius: 50%;
    background: radial-gradient(circle at 50% 50%, #eef5e4 0%, #b7d88c 45%, var(--green) 75%, #ffffff 76%, #ffffff 80%, var(--green-light) 81%, #ffffff 92%);
  }
  .volume {
    position: absolute; left: 30px; top: 662px;
    font-weight: 700; font-size: 28px; line-height: 1; color: var(--ink);
    z-index: 2;
  }
  .band {
    position: absolute; left: 0; bottom: 0; width: 100%; height: 170px;
  }
  .band svg { position: absolute; inset: 0; }
  .claims {
    position: absolute; top: 34px; width: 100%; text-align: center;
    font-weight: 700; font-size: 16px; line-height: 1.15; color: var(--band-text);
    text-transform: uppercase;
  }
  .description {
    position: absolute; top: 98px; left: 18px; right: 18px; text-align: center;
    font-weight: 400; font-size: 15px; line-height: 1.3; color: var(--band-text);
  }
</style>
</head>
<body>
  <main class="label">
    <div class="brand">
      <span class="brand-name">OWRU</span>
      <span class="brand-dot"></span>
    </div>
    <h1 class="product-name">AVOCADO</h1>
    <p class="product-type">smoothie</p>
    <p class="flavour">with Apple &amp; Blueberry</p>
    <div class="hero" role="img" aria-label="Green swirl with a whole avocado, half avocado, red apple and blueberries"></div>
    <p class="volume">300ml</p>
    <section class="band">
      <svg width="520" height="170" viewBox="0 0 520 170" preserveAspectRatio="none" aria-hidden="true">
        <defs>
          <linearGradient id="bandFill" x1="0" y1="0" x2="0" y2="1">
            <stop offset="0" stop-color="#5b9a2c"/>
            <stop offset="1" stop-color="#3f7a1e"/>
          </linearGradient>
        </defs>
        <path d="M0 10 Q260 40 520 10 L520 170 L0 170 Z" fill="url(#bandFill)"/>
      </svg>
      <p class="claims">All natural ingredients,<br>No added sugar or salt,<br>No additives or preservatives</p>
      <p class="description">Made from the finest blend of avocados, to nourish you with a rich, creamy and unique avocado experience that is good and satisfyingly delicious!</p>
    </section>
  </main>
</body>
</html>
```